Business card design for sustainable building and development company

Need a business card design for a new sustainable building and real estate development company in the San Francisco Bay area. Name of company is "Norvale Advisors, LLC" and we provide "Sustainable building, energy and development services" for residential and non residential projects. We'd like the following colors used but not all area required: green, gray, blue. Design should communicate innovation, professionalism and sustainability. Our current website is www.norvale-advisors.example. Another possible design idea is to have the following listed on the back of the card:
Certified: TRAM QX, Leaf Mark Grader, VOLT Grader, EcoState Examiner, RDQ HX Building Analyst. Its not a must but could be text that could be used for back of card. Overall, we are open to a simple, clean design and or one with more text than usual for a card.

Industry/Entity Type

Real Estate

Contact Information for Business Card

Name on card: Dmitri L. Hasby
Title for Name: Principal + Founder
Phone: 555.418.2096
Email: dhasby@norvale-advisors.example
Website: www.norvale-advisors.example

Also, please add the following for address:
Larkport, West Marin

Requirements
Nice to have
• If you can integrate the outline of a skyline on the backside of the card and if it looks good, I would like to see the design
Should not have
• a barcode;

```html
<!DOCTYPE html>
<html lang="en">
<head>
<meta charset="utf-8">
<title>Norvale Advisors — Business Card</title>
<link rel="stylesheet" href="https://fonts.googleapis.com/css2?family=Montserrat:wght@500;700&family=Roboto:wght@400;500;700&display=swap">
<style>
  :root {
    --green: #4aa82c;
    --green-soft: #c6dca3;
    --green-pale: #d8e7c0;
    --ink: #5e5e5e;
    --ink-dark: #3f3f3f;
    --paper: #f7f7f5;
    --backdrop: #dcdcdc;
  }
  * { box-sizing: border-box; margin: 0; padding: 0; }
  html, body { width: 1200px; height: 1029px; overflow: hidden; }
  body { background: var(--backdrop); position: relative; font-family: "Roboto", sans-serif; }

  .card {
    position: absolute;
    left: 200px;
    width: 800px;
    height: 457px;
    background: var(--paper);
    overflow: hidden;
    box-shadow: 0 6px 18px rgba(0,0,0,.18);
  }
  .card--back { top: 40px; }
  .card--front { top: 532px; }

  .decor {
    position: absolute;
    background: linear-gradient(160deg, var(--green-soft), var(--green-pale));
  }
  .card--back .decor { left: 40px; top: 0; width: 290px; height: 457px; }
  .card--front .decor { left: 0; top: 215px; width: 310px; height: 242px; }

  .brand { position: absolute; }
  .brand__row { display: flex; align-items: center; gap: 14px; }
  .brand__dot {
    width: 70px; height: 70px; border-radius: 50%;
    background: var(--green); flex: none;
  }
  .brand__name {
    font-family: "Montserrat", sans-serif; font-weight: 700;
    font-size: 42px; color: var(--green); letter-spacing: .5px; line-height: 1;
  }
  .brand__tagline {
    font-family: "Montserrat", sans-serif; font-weight: 500;
    font-size: 11.5px; color: var(--ink-dark); text-transform: uppercase;
    letter-spacing: .3px; margin: 4px 0 0 84px; white-space: nowrap;
  }
  .card--back .brand { left: 350px; top: 150px; }
  .card--front .brand { left: 40px; top: 48px; }

  .site-url {
    position: absolute; left: 360px; top: 380px;
    font-weight: 500; font-size: 16px; letter-spacing: 1.5px;
    color: var(--green); text-transform: uppercase;
  }

  .contact { position: absolute; left: 400px; top: 250px; }
  .contact__name {
    font-weight: 700; font-size: 26px; letter-spacing: 2px;
    color: var(--ink); text-transform: uppercase; line-height: 1.2;
  }
  .contact__title {
    font-weight: 500; font-size: 16px; letter-spacing: 2px;
    color: var(--green); text-transform: uppercase; margin-bottom: 18px;
  }
  .contact__list { list-style: none; }
  .contact__item {
    display: flex; align-items: center; gap: 14px;
    font-size: 15px; letter-spacing: 1.2px; color: var(--ink);
    text-transform: uppercase; margin-bottom: 10px; white-space: nowrap;
  }
  .contact__icon {
    width: 24px; height: 24px; border-radius: 4px;
    background: var(--green); flex: none;
    display: flex; align-items: center; justify-content: center;
  }
</style>
</head>
<body>

<section class="card card--back" aria-label="Card back">
  <div class="decor" role="img" aria-label="Soft green building illustration"></div>
  <div class="brand">
    <div class="brand__row">
      <span class="brand__dot"></span>
      <span class="brand__name">Norvale Advisors</span>
    </div>
    <p class="brand__tagline">Green design, power &amp; growth advisory services</p>
  </div>
  <p class="site-url">www.norvale-advisors.example</p>
</section>

<section class="card card--front" aria-label="Card front">
  <div class="decor" role="img" aria-label="Soft green building illustration"></div>
  <div class="brand">
    <div class="brand__row">
      <span class="brand__dot"></span>
      <span class="brand__name">Norvale Advisors</span>
    </div>
    <p class="brand__tagline">Green design, power &amp; growth advisory services</p>
  </div>

  <div class="contact">
    <h1 class="contact__name">Dmitri L. Hasby</h1>
    <p class="contact__title">Principal/Owner</p>
    <ul class="contact__list">
      <li class="contact__item">
        <span class="contact__icon">
          <svg width="12" height="16" viewBox="0 0 12 16"><rect x="1" y="1" width="10" height="14" rx="2" fill="none" stroke="#fff" stroke-width="1.6"/><circle cx="6" cy="12.3" r="1" fill="#fff"/></svg>
        </span>555.418.2096
      </li>
      <li class="contact__item">
        <span class="contact__icon">
          <svg width="16" height="12" viewBox="0 0 16 12"><rect x="1" y="1" width="14" height="10" fill="#fff"/><path d="M1 1 L8 7 L15 1" fill="none" stroke="#4aa82c" stroke-width="1.4"/></svg>
        </span>dhasby@norvale-advisors.example
      </li>
      <li class="contact__item">
        <span class="contact__icon">
          <svg width="16" height="16" viewBox="0 0 16 16"><circle cx="8" cy="8" r="6.5" fill="none" stroke="#fff" stroke-width="1.5"/><ellipse cx="8" cy="8" rx="2.8" ry="6.5" fill="none" stroke="#fff" stroke-width="1.2"/><line x1="1.5" y1="8" x2="14.5" y2="8" stroke="#fff" stroke-width="1.2"/></svg>
        </span>www.norvale-advisors.example
      </li>
      <li class="contact__item">
        <span class="contact__icon">
          <svg width="12" height="16" viewBox="0 0 12 16"><path d="M6 15 C6 15 1 9 1 6 A5 5 0 0 1 11 6 C11 9 6 15 6 15 Z" fill="#fff"/><circle cx="6" cy="6" r="1.8" fill="#4aa82c"/></svg>
        </span>Larkport, West Marin
      </li>
    </ul>
  </div>
</section>

</body>
</html>
```